Need a Shopvarnel Design for a new company called DeskRaven

DeskRaven is a new US company that sells compatible toner cartridges and remanufactured ink jet cartridges and other office supplies direct from the manufacturers. We will need to add an app like Gear Locator to the site so that users can search for supplies for their machine model. We need to connect our Quorvex and tilmo inventory with the ShopVarnel site through Syncpyle.

```html
<!DOCTYPE html>
<html lang="en">
<head>
<meta charset="utf-8">
<title>DeskRaven — Compatible Toner &amp; Ink Cartridges</title>
<link href="https://fonts.googleapis.com/css2?family=Poppins:wght@300;400;500;600;700;800;900&display=swap" rel="stylesheet">
<style>
:root{
  --ink:#111111;
  --text:#333333;
  --muted:#666666;
  --white:#ffffff;
  --pink:#f43d96;
  --magenta:#e5288f;
  --blue:#1aa7e6;
  --yellow:#f9ee4a;
  --ghost:#f2f2f2;
  --line:#e3e3e3;
  --soft-pink:#fde0f8;
  --soft-cream:#f7f8dc;
  --soft-grey:#f1f1f1;
  --soft-mint:#e4f1ee;
}
*{margin:0;padding:0;box-sizing:border-box}
html,body{width:1200px;height:3743px;overflow:hidden;background:var(--white)}
body{position:relative;font-family:'Poppins',sans-serif;color:var(--text)}
.abs{position:absolute}
a{color:inherit;text-decoration:none}

/* header */
.brand{left:84px;top:46px;font-size:25px;font-weight:600;color:var(--ink);letter-spacing:-.3px}
.search{left:370px;top:44px;width:452px;height:36px;border:1px solid var(--line);border-radius:18px;padding:0 18px;display:flex;align-items:center;justify-content:space-between;font-size:11px;color:#999}
.header-icon{top:48px}
.currency{left:1010px;top:48px;display:flex;align-items:center;gap:7px;font-size:11px;font-weight:600;color:var(--ink)}
.flag-dot{width:28px;height:28px;border-radius:50%;background:linear-gradient(135deg,#1f3f8f,#c8102e)}

/* hero */
.hero{left:0;top:126px;width:1200px;height:577px;background:var(--pink)}
.hero-art{left:640px;top:126px;width:470px;height:520px;border-radius:6px;background:radial-gradient(ellipse at 55% 70%,#f4f4f4 0 28%,rgba(255,255,255,.2) 52%,transparent 70%),linear-gradient(120deg,#ff3b3b,#ffd43b,#38d35a,#2f8cff,#a34dff)}
.hero-title{left:122px;top:282px;font-size:54px;line-height:62px;font-weight:800;color:var(--white);white-space:nowrap}
.hero-text{left:122px;top:424px;width:450px;font-size:11.5px;line-height:20.5px;color:var(--white)}
.btn{display:flex;align-items:center;justify-content:center;gap:6px;border-radius:22px;font-size:11px;font-weight:600;text-transform:uppercase}
.btn-light{left:126px;top:509px;width:159px;height:42px;background:var(--white);color:var(--ink)}
.btn-outline{left:301px;top:509px;width:159px;height:42px;border:2px solid var(--white);color:var(--white)}
.dots{left:580px;top:662px;display:flex;gap:8px}
.dots span{width:11px;height:11px;border-radius:50%;background:var(--white)}
.dots span:first-child{background:transparent;border:2px solid var(--white)}

/* about */
.about-ghost{left:1032px;top:770px;font-size:150px;font-weight:900;color:var(--ghost);writing-mode:vertical-rl;line-height:116px;letter-spacing:4px}
.about-frame{left:83px;top:831px;width:415px;height:446px;border:4px solid var(--blue);border-right:none}
.about-frame-right{left:494px;width:4px;background:var(--blue)}
.about-art{left:94px;top:872px;width:393px;height:356px;background:radial-gradient(circle at 50% 55%,#3b8ee0 0 32%,#d8e8f8 45%,#ffffff 70%)}
.section-title{font-size:32px;font-weight:800;color:var(--ink)}
.about-title{left:487px;top:955px}
.about-text{left:488px;top:1019px;width:500px;font-size:11.5px;line-height:20.5px;color:var(--text)}
.about-link{left:488px;top:1132px;font-size:11px;font-weight:600;color:var(--ink)}

/* products */
.products-title{left:0;top:1386px;width:1200px;text-align:center}
.tabs{left:0;top:1447px;width:1200px;display:flex;justify-content:center;gap:36px;font-size:12px;color:var(--muted)}
.tabs .active{color:var(--ink);font-weight:500}
.card-img{width:231px;height:246px}
.badge{background:var(--ink);color:var(--white);font-size:10.5px;font-weight:600;padding:2px 9px}
.card-name{font-size:12px;font-weight:500;color:var(--ink)}
.card-price{font-size:11.5px;color:var(--text)}
.cart-sep{width:1px;height:20px;background:var(--line)}
.quick-actions{left:548px;top:1537px;width:38px;height:115px;background:var(--white);border:1px solid var(--line);display:flex;flex-direction:column}
.quick-actions span{flex:1;display:flex;align-items:center;justify-content:center;border-bottom:1px solid var(--line)}
.quick-actions span:last-child{border-bottom:none}
.card-detail{left:354px;top:1780px;width:232px;height:94px;background:#f5f5f5}

/* testimonials */
.reviews-ghost{left:0;top:2282px;width:1200px;text-align:center;font-size:160px;font-weight:900;color:var(--ghost);letter-spacing:2px;line-height:170px}
.testimonials-title{left:0;top:2342px;width:1200px;text-align:center}
.quote-card{top:2502px;width:471px;height:246px;border:3px solid}
.quote-card.pink{left:106px;border-color:var(--magenta)}
.quote-card.blue{left:620px;border-color:var(--blue)}
.quote-gap{top:-4px;left:178px;width:115px;height:6px;background:var(--white)}
.avatar{top:-31px;left:207px;width:56px;height:56px;border-radius:50%;background:radial-gradient(circle,#d9c8b8,#a8988a);border:3px solid var(--white)}
.quote-text{left:40px;top:50px;width:385px;text-align:center;font-size:14px;line-height:26px;color:var(--text)}
.quote-by{left:0;top:185px;width:465px;text-align:center;font-size:11px;color:var(--text)}
.quote-by b{font-weight:600;color:var(--ink)}
.arrow{top:2783px;width:28px;height:28px;border-radius:50%;background:var(--ink);display:flex;align-items:center;justify-content:center}

/* toner band */
.band{left:0;top:2877px;width:1200px;height:385px;background:var(--yellow)}
.band-art{left:73px;top:2913px;width:668px;height:335px;background:linear-gradient(100deg,#27c6e8 0 22%,#e52b9d 22% 44%,#f6d91c 44% 66%,#2a2a2a 66% 90%,transparent 90%);border-radius:8px;opacity:.9}
.band-title{right:113px;top:2935px;text-align:right;font-size:54px;line-height:62px;font-weight:800;color:var(--ink)}
.band-text{right:113px;top:3080px;width:330px;text-align:right;font-size:11.5px;line-height:20.5px;color:var(--text)}
.btn-dark{left:927px;top:3163px;width:160px;height:41px;background:var(--ink);color:var(--white)}

/* footer */
.footer-brand{left:84px;top:3352px;font-size:25px;font-weight:600;color:var(--ink)}
.footer-text{left:84px;top:3408px;width:270px;font-size:11.5px;line-height:20.7px;color:var(--muted)}
.payments{left:80px;top:3600px;display:flex;gap:24px;align-items:center;font-size:14px;font-weight:600;color:#1c3f94}
.payments span:first-child{display:flex;align-items:center;gap:6px}
.payments i{display:inline-block;width:14px;height:14px;border-radius:50%;background:#f0651f}
.footer-head{top:3364px;font-size:13px;font-weight:500;color:var(--ink)}
.footer-links{top:3414px;list-style:none;font-size:12px;line-height:30.5px;color:var(--muted)}
.footer-sub{left:822px;top:3392px;font-size:11.5px;color:var(--muted)}
.newsletter{left:820px;top:3435px;width:313px;height:35px;border:1px solid var(--line);border-radius:18px;padding:0 16px;display:flex;align-items:center;justify-content:space-between;font-size:11px;color:#999}
.socials{left:823px;top:3498px;display:flex;gap:7px}
.socials span{width:30px;height:30px;border-radius:50%;border:2px solid var(--ink)}
.copyright{left:824px;top:3588px;font-size:11.5px;color:var(--muted)}
.copyright b{font-weight:600;color:var(--ink)}
</style>
</head>
<body>

<header>
  <div class="abs brand">DeskRaven</div>
  <div class="abs search">
    <span>OEM Part No. / Model / Keyword</span>
    <svg width="20" height="20" viewBox="0 0 20 20" fill="none" stroke="#111" stroke-width="1.6"><circle cx="8.5" cy="8.5" r="6.5"/><path d="M13.5 13.5L18 18"/></svg>
  </div>
  <svg class="abs header-icon" style="left:894px" width="22" height="24" viewBox="0 0 22 24" fill="none" stroke="#111" stroke-width="1.5"><circle cx="11" cy="7" r="5"/><path d="M2 22c0-5 4-8 9-8s9 3 9 8z"/></svg>
  <svg class="abs header-icon" style="left:946px;top:44px" width="32" height="28" viewBox="0 0 32 28" fill="none" stroke="#111" stroke-width="1.5"><path d="M1 6h4l3 12h13l3-9H7"/><circle cx="10" cy="23" r="2"/><circle cx="19" cy="23" r="2"/><circle cx="26" cy="6" r="5" fill="#111" stroke="none"/><text x="26" y="8.5" font-size="7" fill="#fff" stroke="none" text-anchor="middle" font-family="Poppins,sans-serif">0</text></svg>
  <div class="abs currency"><span class="flag-dot"></span>GBP <svg width="8" height="6" viewBox="0 0 8 6" fill="none" stroke="#111" stroke-width="1.2"><path d="M1 1l3 3 3-3"/></svg></div>
  <svg class="abs" style="left:1108px;top:53px" width="17" height="14" viewBox="0 0 17 14" stroke="#111" stroke-width="2"><path d="M0 1h17M0 7h17M0 13h17"/></svg>
</header>

<section>
  <div class="abs hero"></div>
  <div class="abs hero-art" role="img" aria-label="Four ink jet cartridges resting on a rainbow ribbon of colour grid paper"></div>
  <h1 class="abs hero-title">INK JET<br>CARTRIDGES</h1>
  <p class="abs hero-text">DeskRaven is a new US company that sells compatible toner cartridges and remanufactured ink jet cartridges and other office supplies direct from the manufacturers.</p>
  <a class="abs btn btn-light">Learn More</a>
  <a class="abs btn btn-outline"><svg width="13" height="13" viewBox="0 0 13 13" fill="none" stroke="#fff" stroke-width="1.5"><circle cx="8" cy="5" r="4"/><path d="M5 8l-4 4"/></svg>Supplies</a>
  <div class="abs dots"><span></span><span></span><span></span></div>
</section>

<section>
  <div class="abs about-ghost">ABOUT</div>
  <div class="abs about-frame"></div>
  <div class="abs about-frame-right" style="top:831px;height:76px"></div>
  <div class="abs about-frame-right" style="top:1220px;height:57px"></div>
  <div class="abs about-art" role="img" aria-label="Blue recycling bin filled with used ink cartridges"></div>
  <h2 class="abs section-title about-title">ABOUT US</h2>
  <p class="abs about-text">Donec accumsan auctor iaculis. Sed suscipit arcu ligula, at egestas magna molestie a. Proin ac ex maximus ultrices justo eget, sodales orci. Faucibus ac laoreet sed. Aliquam egestas libero ac turpis pharetra, in vehicula lacus scelerisque. Vestibulum ut sem laoreet, feugiat tellus at, hendrerit arcu.</p>
  <a class="abs about-link">LEARN MORE</a>
</section>

<section>
  <h2 class="abs section-title products-title">OUR PRODUCTS</h2>
  <div class="abs tabs"><span class="active">Toner cartridges</span><span>Ink jet cartridges</span><span>Office supplies</span></div>

  <div class="abs card-img" style="left:93px;top:1534px;background:var(--soft-pink)" role="img" aria-label="Set of colour toner cartridges"></div>
  <span class="abs badge" style="left:282px;top:1535px">New</span>
  <div class="abs card-detail"></div>
  <div class="abs card-img" style="left:354px;top:1534px;background:var(--blue)" role="img" aria-label="Row of four ink jet cartridges"></div>
  <div class="abs quick-actions">
    <span><svg width="18" height="16" viewBox="0 0 18 16" fill="none" stroke="#111" stroke-width="1.3"><path d="M1 2h3l2 8h8l2-6H5"/><circle cx="7" cy="13" r="1.3"/><circle cx="13" cy="13" r="1.3"/></svg></span>
    <span><svg width="16" height="18" viewBox="0 0 16 18" fill="none" stroke="#111" stroke-width="1.3"><circle cx="8" cy="5" r="4"/><path d="M1 17c0-4 3-6 7-6s7 2 7 6z"/></svg></span>
    <span><svg width="16" height="16" viewBox="0 0 16 16" fill="none" stroke="#111" stroke-width="1.3"><circle cx="7" cy="7" r="5"/><path d="M11 11l4 4"/></svg></span>
  </div>
  <div class="abs card-img" style="left:613px;top:1534px;background:var(--soft-cream)" role="img" aria-label="Black laser toner cartridge"></div>
  <span class="abs badge" style="left:802px;top:1535px">New</span>
  <div class="abs card-img" style="left:873px;top:1534px;background:var(--soft-grey)" role="img" aria-label="Set of colour toner cartridges"></div>

  <span class="abs card-name" style="left:94px;top:1797px">Toner cartridges</span>
  <span class="abs card-price" style="left:94px;top:1817px">$35.00</span>
  <span class="abs cart-sep" style="left:283px;top:1796px"></span>
  <span class="abs card-name" style="left:366px;top:1797px">Ink jet cartridges</span>
  <span class="abs card-price" style="left:493px;top:1797px">$35.00</span>
  <p class="abs" style="left:366px;top:1826px;width:200px;font-size:10px;line-height:12px">Donec accumsan auctor iaculis. Sed suscipit arcu ligula, at egestas</p>
  <span class="abs card-name" style="left:614px;top:1797px">Toner cartridges</span>
  <span class="abs card-price" style="left:614px;top:1817px">$35.00</span>
  <span class="abs cart-sep" style="left:803px;top:1796px"></span>
  <span class="abs card-name" style="left:873px;top:1797px">Toner cartridges</span>
  <span class="abs card-price" style="left:873px;top:1817px">$35.00</span>
  <span class="abs cart-sep" style="left:1062px;top:1796px"></span>

  <div class="abs card-img" style="left:93px;top:1904px;background:var(--soft-cream)" role="img" aria-label="Set of colour toner cartridges"></div>
  <div class="abs card-img" style="left:354px;top:1904px;background:var(--soft-grey)" role="img" aria-label="Black laser toner cartridge"></div>
  <span class="abs badge" style="left:545px;top:1905px">New</span>
  <div class="abs card-img" style="left:613px;top:1904px;background:var(--soft-mint)" role="img" aria-label="Row of four ink jet cartridges"></div>
  <div class="abs card-img" style="left:873px;top:1904px;background:var(--soft-pink)" role="img" aria-label="Set of colour toner cartridges"></div>
  <span class="abs badge" style="left:1062px;top:1905px">New</span>

  <span class="abs card-name" style="left:94px;top:2170px">Toner cartridges</span>
  <span class="abs card-price" style="left:94px;top:2190px">$35.00</span>
  <span class="abs cart-sep" style="left:283px;top:2169px"></span>
  <span class="abs card-name" style="left:353px;top:2170px">Toner cartridges</span>
  <span class="abs card-price" style="left:353px;top:2190px">$35.00</span>
  <span class="abs cart-sep" style="left:543px;top:2169px"></span>
  <span class="abs card-name" style="left:614px;top:2170px">Toner cartridges</span>
  <span class="abs card-price" style="left:614px;top:2190px">$35.00</span>
  <span class="abs cart-sep" style="left:803px;top:2169px"></span>
  <span class="abs card-name" style="left:873px;top:2170px">Toner cartridges</span>
  <span class="abs card-price" style="left:873px;top:2190px">$35.00</span>
  <span class="abs cart-sep" style="left:1062px;top:2169px"></span>

  <svg width="0" height="0" style="position:absolute"><defs><g id="cart"><path d="M1 2h3l2 8h8l2-6H5" fill="none" stroke="#111" stroke-width="1.3"/><circle cx="7" cy="13" r="1.3" fill="none" stroke="#111" stroke-width="1.3"/><circle cx="13" cy="13" r="1.3" fill="none" stroke="#111" stroke-width="1.3"/></g></defs></svg>
  <svg class="abs" style="left:300px;top:1797px" width="18" height="16"><use href="#cart"/></svg>
  <svg class="abs" style="left:555px;top:1797px" width="18" height="16"><use href="#cart"/></svg>
  <svg class="abs" style="left:820px;top:1797px" width="18" height="16"><use href="#cart"/></svg>
  <svg class="abs" style="left:1080px;top:1797px" width="18" height="16"><use href="#cart"/></svg>
  <svg class="abs" style="left:300px;top:2170px" width="18" height="16"><use href="#cart"/></svg>
  <svg class="abs" style="left:560px;top:2170px" width="18" height="16"><use href="#cart"/></svg>
  <svg class="abs" style="left:820px;top:2170px" width="18" height="16"><use href="#cart"/></svg>
  <svg class="abs" style="left:1080px;top:2170px" width="18" height="16"><use href="#cart"/></svg>
</section>

<section>
  <div class="abs reviews-ghost">REVIEWS</div>
  <h2 class="abs section-title testimonials-title">TESTIMONIALS</h2>
  <div class="abs quote-card pink">
    <span class="abs quote-gap"></span>
    <span class="abs avatar" role="img" aria-label="Customer portrait"></span>
    <p class="abs quote-text">“ Donec accumsan auctor iaculis. Sed suscipit arcu ligula, at egestas magna molestie a. Proin ac ex maximus ultrices justo eget, sodales orci. Faucibus ac laoreet sed. Aliquam egestas libero ac turpis</p>
    <p class="abs quote-by"><b>Dana Whitlow</b> &nbsp;-&nbsp; Manhattan, New York</p>
  </div>
  <div class="abs quote-card blue">
    <span class="abs quote-gap"></span>
    <span class="abs avatar" role="img" aria-label="Customer portrait"></span>
    <p class="abs quote-text">“ Donec accumsan auctor iaculis. Sed suscipit arcu ligula, at egestas magna molestie a. Proin ac ex maximus ultrices justo eget, sodales orci. Faucibus ac laoreet sed. Aliquam egestas libero ac turpis</p>
    <p class="abs quote-by"><b>Dana Whitlow</b> &nbsp;-&nbsp; Manhattan, New York</p>
  </div>
  <span class="abs arrow" style="left:567px"><svg width="12" height="8" viewBox="0 0 12 8" fill="none" stroke="#fff" stroke-width="1.3"><path d="M12 4H1M4 1L1 4l3 3"/></svg></span>
  <span class="abs arrow" style="left:605px"><svg width="12" height="8" viewBox="0 0 12 8" fill="none" stroke="#fff" stroke-width="1.3"><path d="M0 4h11M8 1l3 3-3 3"/></svg></span>
</section>

<section>
  <div class="abs band"></div>
  <div class="abs band-art" role="img" aria-label="Cyan, magenta, yellow and black toner cartridges lying side by side"></div>
  <h2 class="abs band-title">TONER<br>CARTRIDGES</h2>
  <p class="abs band-text">Donec accumsan auctor iaculis. Sed suscipit arcu ligula, at egestas magna molestie a. Proin ac ex maximus ultrices justo eget, sodales orci.</p>
  <a class="abs btn btn-dark">Learn More</a>
</section>

<footer>
  <div class="abs footer-brand">DeskRaven</div>
  <p class="abs footer-text">Donec accumsan auctor iaculis. Sed suscipit arcu ligula, at egestas magna molestie a. Proin ac ex maximus ultrices justo eget, sodales orci. Faucibus ac laoreet sed. Aliquam egestas libero ac turpis pharetra, in vehicula lacus scelerisque. Vestibulum ut sem laoreet, feugiat tellus at, hendrerit arcu.</p>
  <div class="abs payments"><span><i></i>Cardlo</span><span>Payvio</span><span>Tallypay</span><span>Nimbpay</span></div>

  <h3 class="abs footer-head" style="left:442px">Useful Links</h3>
  <ul class="abs footer-links" style="left:441px">
    <li>Search</li><li>About Us</li><li>Contact Us</li><li>Payment Info</li><li>Delivery</li><li>Return and Refund Policy</li><li>Privacy Policy</li><li>Terms &amp; Conditions</li>
  </ul>
  <h3 class="abs footer-head" style="left:634px">Categories</h3>
  <ul class="abs footer-links" style="left:633px">
    <li>Toner cartridges</li><li>Ink jet cartridges</li><li>Office supplies</li>
  </ul>

  <h3 class="abs footer-head" style="left:822px;top:3362px">Be in the know</h3>
  <p class="abs footer-sub">Sign up for the latest news, offers and styles</p>
  <div class="abs newsletter"><span>Your Mail Address</span><svg width="12" height="8" viewBox="0 0 12 8" fill="none" stroke="#111" stroke-width="1.2"><path d="M0 4h11M8 1l3 3-3 3"/></svg></div>
  <div class="abs socials">
    <span style="background:var(--blue)"></span><span style="background:var(--magenta)"></span><span style="background:var(--yellow)"></span><span style="background:var(--white)"></span>
  </div>
  <p class="abs copyright">© 2021, <b>DeskRaven.</b> All Rights Reserved.</p>
</footer>

</body>
</html>
```